Progressive European Honey Business needs minimalistic packaging design

Hello - thank you for your interest in our brief. We are Fizzy Vixens, a London based Honey business, importing only the best honey Europe has to offer. Our values are deeply rooted with in progressive liberal values and we are looking for minimalist packaging, which reflects that.

We are looking for a design, which dimensions fit with our packaging option (Velmor Glass Jar | HEIGHT 90mm | DIAMETER 63mm). We will require a various output files (High Resolution JPEG (CMYK Colors 300 dpi) Source File Ai, PSD, PDF, Printing files (die cut, die folding) and a 3D Mockup of the packaging for use within digital commerce platforms.

We must be able to adjust the free text on the label front and it should include the following:
Brand Name
Honey type
Limited edition No. X / 100 ( X being the number of purchase i.e. 25 / 100)
EU Honey, Single Orgin (Germany)
(c) The net weight (250g)

The back must include room for additional information (again adjustable by us) and the following:
“Unsuitable for children under 12 months”
(b) The appropriate durability declaration

In total, we are looking for
a) A front label
b) A back label
c) A seal (round) including the attached bee and logo included in the Zip file.
Do note that a) & b) can also be combined into one design as long as the symmetry on the jar stays intact.

The final design should communicate modern aesthetics, high quality, that are slightly provocative and pop off the shelves.

Hi folks, sorry for the delay in completing this project, but my business partner had a leak in his house. We planned to finalise our review today, but this will have to wait until it's no longer raining in his livingroom. Our sincere apologies!

• See branding guidelines

• Must follow the branding guideline and fonts provided as attachment

```html
<!DOCTYPE html>
<html lang="en">
<head>
<meta charset="utf-8">
<title>Fizzy Vixens – Jar Label</title>
<link href="https://fonts.googleapis.com/css2?family=Barlow+Condensed:wght@600;800&family=Mukta:wght@500&display=swap" rel="stylesheet">
<style>
  :root {
    --page: #f2f2f2;
    --label-white: #ffffff;
    --honey-deep: #e9961e;
    --honey-mid: #f6b53a;
    --badge-yellow: #ffd21a;
    --badge-gold: #f5b400;
    --ink: #0b0b0b;
    --text: #1c1c1c;
  }
  html, body {
    margin: 0;
    padding: 0;
    width: 1200px;
    height: 1070px;
    overflow: hidden;
    background: var(--page);
  }
  .canvas {
    position: relative;
    width: 1200px;
    height: 1070px;
  }
  .jar-label {
    position: absolute;
    left: 80px;
    top: 371px;
    width: 1040px;
    height: 328px;
    overflow: visible;
  }
  .info-text {
    font-family: "Mukta", sans-serif;
    font-weight: 500;
    font-size: 19px;
    fill: var(--text);
    text-anchor: middle;
  }
  .brand-name {
    font-family: "Barlow Condensed", sans-serif;
    font-weight: 800;
    font-size: 54px;
    fill: var(--badge-gold);
    text-anchor: middle;
    letter-spacing: 1px;
  }
  .origin-text {
    font-family: "Barlow Condensed", sans-serif;
    font-weight: 600;
    font-size: 28px;
    fill: var(--label-white);
    text-anchor: middle;
  }
</style>
</head>
<body>
<div class="canvas">
  <svg class="jar-label" viewBox="0 0 1040 328" xmlns="http://www.w3.org/2000/svg">
    <defs>
      <linearGradient id="honeyFade" x1="0" y1="0" x2="0" y2="1">
        <stop offset="0" stop-color="var(--honey-deep)"/>
        <stop offset="0.45" stop-color="var(--honey-mid)"/>
        <stop offset="1" stop-color="#ffffff"/>
      </linearGradient>
      <radialGradient id="badgeGlow" cx="0.5" cy="0.4" r="0.6">
        <stop offset="0" stop-color="var(--badge-yellow)"/>
        <stop offset="1" stop-color="var(--badge-gold)"/>
      </radialGradient>
      <clipPath id="sealInner">
        <circle cx="520" cy="186" r="124"/>
      </clipPath>
    </defs>

    <!-- label base -->
    <rect class="label-base" x="0" y="0" width="1040" height="328" fill="var(--label-white)"/>

    <!-- honeycomb band -->
    <rect class="honeycomb-band" x="0" y="0" width="1040" height="185" fill="url(#honeyFade)"
          role="img" aria-label="Honeycomb pattern fading from amber to white"/>

    <!-- ribbon strip behind the seal -->
    <rect class="seal-ribbon" x="464" y="0" width="112" height="80" fill="var(--badge-yellow)"/>

    <!-- seal -->
    <g class="seal">
      <circle cx="520" cy="186" r="150" fill="url(#badgeGlow)"/>
      <circle cx="520" cy="186" r="130" fill="var(--ink)"/>
      <g clip-path="url(#sealInner)">
        <rect x="390" y="50" width="260" height="152" fill="var(--label-white)"/>
        <rect x="390" y="202" width="260" height="120" fill="var(--ink)"/>
      </g>
      <text class="brand-name" x="520" y="142">FIZZY</text>
      <text class="brand-name" x="520" y="192">VIXENS</text>
      <text class="origin-text" x="520" y="236">EU HONEY</text>
      <text class="origin-text" x="520" y="268">SINGLE ORGIN</text>
    </g>

    <!-- back panel info -->
    <g class="info-left">
      <text class="info-text" x="174" y="197">Unsuitable for children</text>
      <text class="info-text" x="174" y="220">under 12 months</text>
      <line x1="68" y1="236" x2="280" y2="236" stroke="var(--ink)" stroke-width="2.5"/>
      <text class="info-text" x="174" y="264">Limited edition No. X / 100</text>
    </g>
    <g class="info-right">
      <text class="info-text" x="870" y="197">The appropriate</text>
      <text class="info-text" x="870" y="220">durability declaration</text>
      <line x1="764" y1="236" x2="976" y2="236" stroke="var(--ink)" stroke-width="2.5"/>
      <text class="info-text" x="870" y="264">Net Weight (250g)</text>
    </g>
  </svg>
</div>
</body>
</html>
```